New Business Card

We need to refresh our business cards. We designed these ourselves and we have no graphic design experience. We would like to find a new business card design that is professional and unique. We are an auto finance company. Feel free to play with the logo, but we would like to keep the eye very present on the card. Our corporate colors are green, grey, and white.
Green - RGB - 168,215,27; HEX - #AADD22
Grey - RGB - 196,196,196; HEX - #C4C4C4
Need to upload the vector file to finalize the project. The last logo was for a jpeg that didn't stretch well.
Industry/Entity Type
Financial Service
Contact Information for Business Card
Honestly don't know...I need your help!

```html
<!DOCTYPE html>
<html lang="en">
<head>
<meta charset="utf-8">
<title>Northlook Capital – Business Card</title>
<link rel="stylesheet" href="https://fonts.googleapis.com/css2?family=Lora:wght@400;700&display=swap">
<style>
  :root {
    --page-bg: #e4e1dc;
    --card-light: #f1efec;
    --card-light-edge: #dcd8d3;
    --green-deep: #4f8a14;
    --green-mid: #6aa81f;
    --green-bright: #82c12c;
    --brand-green: #78b22a;
    --arc-grey: #a9a4a0;
    --arc-pale: #d9d1cc;
    --text-on-green: #e6eccf;
    --text-on-green-soft: #d6e2b6;
  }
  * { box-sizing: border-box; margin: 0; padding: 0; }
  html, body {
    width: 1200px;
    height: 970px;
    overflow: hidden;
    background: var(--page-bg);
  }
  .canvas {
    position: relative;
    width: 1200px;
    height: 970px;
  }
  .card {
    position: absolute;
    left: 100px;
    top: 200px;
    width: 1000px;
    height: 570px;
    border-radius: 28px;
    overflow: hidden;
    background: linear-gradient(160deg, var(--card-light) 0%, #e9e6e3 60%, var(--card-light-edge) 100%);
    box-shadow: 0 18px 40px rgba(0,0,0,0.18);
    font-family: "Lora", Georgia, serif;
  }
  .card-shapes {
    position: absolute;
    inset: 0;
    width: 1000px;
    height: 570px;
  }
  .brand {
    position: absolute;
    left: 60px;
    top: 300px;
    width: 380px;
    display: flex;
    align-items: center;
    justify-content: center;
    gap: 14px;
  }
  .brand-dot {
    width: 30px;
    height: 30px;
    border-radius: 50%;
    background: var(--brand-green);
    flex: none;
  }
  .brand-name {
    font-size: 40px;
    font-weight: 700;
    color: var(--brand-green);
    letter-spacing: 0.3px;
    white-space: nowrap;
  }
  .contact {
    position: absolute;
    left: 597px;
    top: 126px;
    color: var(--text-on-green);
  }
  .person-name {
    font-size: 31px;
    font-weight: 700;
    line-height: 1;
  }
  .person-role {
    font-size: 25px;
    line-height: 1.1;
    color: var(--text-on-green-soft);
  }
  .address {
    margin-top: 62px;
    font-size: 25px;
    line-height: 32px;
  }
  .lines {
    margin-top: 20px;
    list-style: none;
    font-size: 24px;
    line-height: 34px;
  }
  .lines li {
    display: flex;
    align-items: center;
    gap: 10px;
  }
  .line-icon {
    width: 28px;
    height: 28px;
    flex: none;
  }
</style>
</head>
<body>
<main class="canvas">
  <section class="card" aria-label="Business card for Northlook Capital">
    <svg class="card-shapes" viewBox="0 0 1000 570" aria-hidden="true">
      <defs>
        <linearGradient id="greenPanel" x1="0" y1="0" x2="1" y2="1">
          <stop offset="0" stop-color="var(--green-deep)"/>
          <stop offset="0.45" stop-color="var(--green-mid)"/>
          <stop offset="0.75" stop-color="var(--green-bright)"/>
          <stop offset="1" stop-color="var(--green-mid)"/>
        </linearGradient>
        <radialGradient id="lightGlow" cx="0.25" cy="0.3" r="0.6">
          <stop offset="0" stop-color="#f8f8f9"/>
          <stop offset="1" stop-color="#ebe6e2" stop-opacity="0"/>
        </radialGradient>
      </defs>
      <rect width="1000" height="570" fill="url(#lightGlow)"/>
      <path class="arc-outer" d="M492 0 C 570 70, 590 220, 556 330 C 520 440, 470 520, 418 570"
            fill="none" stroke="var(--arc-pale)" stroke-width="14"/>
      <path class="arc-grey" d="M480 0 C 556 70, 576 220, 543 330 C 508 440, 456 520, 404 570"
            fill="none" stroke="var(--arc-grey)" stroke-width="10"/>
      <path class="green-panel" d="M466 0 L1000 0 L1000 570 L392 570 C 444 520, 496 440, 530 330 C 562 220, 542 70, 466 0 Z"
            fill="url(#greenPanel)"/>
    </svg>

    <div class="brand">
      <span class="brand-dot"></span>
      <span class="brand-name">Northlook Capital</span>
    </div>

    <div class="contact">
      <p class="person-name">Daniel Reeve</p>
      <p class="person-role">Founder</p>
      <p class="address">PO BOX 480 Harbour Lane<br>7th street Geelong</p>
      <ul class="lines">
        <li>
          <svg class="line-icon" viewBox="0 0 28 28" aria-hidden="true">
            <circle cx="14" cy="14" r="12" fill="none" stroke="currentColor" stroke-width="1.6"/>
            <path d="M9 11 C9 9 11 8.5 14 8.5 C17 8.5 19 9 19 11 L17 12 L16 10.5 L12 10.5 L11 12 Z M10 13 L18 13 L19 19 L9 19 Z" fill="currentColor"/>
          </svg>
          <span>(555) 013-2468</span>
        </li>
        <li>
          <svg class="line-icon" viewBox="0 0 28 28" aria-hidden="true">
            <circle cx="14" cy="14" r="12" fill="none" stroke="currentColor" stroke-width="1.6"/>
            <rect x="8" y="9.5" width="12" height="9" fill="currentColor"/>
            <path d="M8 9.5 L14 14.5 L20 9.5" fill="none" stroke="var(--green-mid)" stroke-width="1.4"/>
          </svg>
          <span>hello@northlookmail.com</span>
        </li>
        <li>
          <svg class="line-icon" viewBox="0 0 28 28" aria-hidden="true">
            <circle cx="14" cy="14" r="12" fill="none" stroke="currentColor" stroke-width="1.6"/>
            <circle cx="14" cy="14" r="6.5" fill="none" stroke="currentColor" stroke-width="1.3"/>
            <path d="M7.5 14 H20.5 M14 7.5 V20.5 M14 7.5 C11 10 11 18 14 20.5 M14 7.5 C17 10 17 18 14 20.5" fill="none" stroke="currentColor" stroke-width="1"/>
          </svg>
          <span>www.northlookcapital.com</span>
        </li>
      </ul>
    </div>
  </section>
</main>
</body>
</html>
```